Business card design needed

am looking for a fun and funky design to match our moto, seriously fun swimwear and fashion for girls.

We manufacture and retail girls swimwear and fashion in Australia. Our designs are fun loving and funky. I would like to use bright fuschia to match our website www.breezyplum.com.au. We target a higher end market so need it to reflect this.

Industry/Entity Type

Fashion

Contact Information for Business Card

Breezy Plum logo,
Maddie Lorne
(07) 35517204
admin@breezyplum.com.au
www.breezyplum.com.au

Logo Text

Breezy Plum

```html
<!DOCTYPE html>
<html lang="en">
<head>
<meta charset="utf-8">
<title>Breezy Plum — Business Card</title>
<link rel="stylesheet" href="https://fonts.googleapis.com/css2?family=Dancing+Script:wght@500&family=Arimo:wght@400&display=swap">
<style>
  :root {
    --stage: #262626;
    --blush: #fbe3ea;
    --blush-line: #f4c2d1;
    --studio: #efe4e9;
    --rose: #ef8fae;
    --fuchsia: #e0306f;
    --fuchsia-deep: #c81d5a;
    --fuchsia-line: #b5164f;
    --ribbon: #ee7a9e;
    --ribbon-light: #f7b3c7;
    --skin: #e2b59f;
    --ink: #111111;
  }
  * { margin: 0; padding: 0; box-sizing: border-box; }
  html, body { width: 1200px; height: 1200px; overflow: hidden; }
  body {
    background: var(--stage);
    position: relative;
    font-family: "Arimo", Arial, sans-serif;
  }
  .card {
    position: absolute;
    left: 150px;
    width: 900px;
    height: 514px;
    overflow: hidden;
    border-radius: 2px;
    box-shadow: 0 12px 30px rgba(0,0,0,0.45);
  }
  .card--front { top: 60px; background: var(--studio); }
  .card--back {
    top: 626px;
    background:
      repeating-linear-gradient(90deg, rgba(255,255,255,0) 0 6px, var(--blush-line) 6px 8px),
      linear-gradient(135deg, #fdf0f4 0%, var(--blush) 50%, #f8cfdb 100%);
  }

  /* shared striped band */
  .band {
    position: absolute; left: 0; width: 100%;
    background:
      repeating-linear-gradient(90deg, rgba(0,0,0,0) 0 5px, rgba(181,22,79,0.45) 5px 7px),
      linear-gradient(180deg, var(--fuchsia) 0%, var(--fuchsia-deep) 100%);
  }
  .ribbon {
    position: absolute; left: 0; width: 100%;
    background: linear-gradient(180deg, var(--ribbon-light) 0%, var(--ribbon) 60%, #e56890 100%);
  }
  .bow {
    position: absolute;
    border-radius: 46% 46% 40% 40% / 60% 60% 40% 40%;
    background: linear-gradient(160deg, var(--ribbon-light) 0%, var(--ribbon) 55%, #d9507c 100%);
    border: 2px solid #d9507c;
  }

  /* front */
  .front__photo {
    position: absolute; left: 0; top: 0; width: 100%; height: 330px;
    background: linear-gradient(180deg, #f3ecef 0%, #eadde3 100%);
  }
  .front__pose {
    position: absolute; width: 150px; border-radius: 70px 70px 10px 10px;
    background: linear-gradient(180deg, var(--skin) 0%, #f5bfd0 35%, #fbe4ec 70%, #f4c9d7 100%);
  }
  .front__pose--one { left: 80px; top: 150px; height: 200px; }
  .front__pose--two { left: 340px; top: 70px; height: 280px; }
  .front__pose--three { left: 600px; top: 30px; height: 240px; }
  .front__ribbon { top: 270px; height: 26px; }
  .front__band { top: 296px; height: 218px; }
  .front__bow { left: 140px; top: 300px; width: 320px; height: 150px; }
  .front__wordmark {
    position: absolute; right: 36px; top: 178px;
    font-family: "Dancing Script", cursive;
    font-weight: 500; font-size: 108px; line-height: 1;
    color: var(--fuchsia);
  }

  /* back */
  .back__wordmark {
    position: absolute; left: 150px; top: 36px;
    font-family: "Dancing Script", cursive;
    font-weight: 500; font-size: 100px; line-height: 1;
    color: var(--fuchsia);
  }
  .back__name {
    position: absolute; left: 300px; top: 156px;
    font-size: 30px; letter-spacing: 7px; text-transform: uppercase;
    color: var(--fuchsia);
  }
  .back__contact {
    position: absolute; left: 200px; top: 202px; width: 440px;
    list-style: none; font-size: 24px; letter-spacing: 3.5px; line-height: 34px;
    color: var(--ink); text-align: center;
  }
  .back__ribbon { top: 312px; height: 44px; }
  .back__band { top: 356px; height: 158px; }
  .back__bow { left: 300px; top: 318px; width: 280px; height: 130px; }
</style>
</head>
<body>
  <section class="card card--front">
    <div class="front__photo" role="img" aria-label="Studio photo backdrop for a model in pink swimwear and patterned leggings">
      <div class="front__pose front__pose--one" role="img" aria-label="Model pose one, hands raised"></div>
      <div class="front__pose front__pose--two" role="img" aria-label="Model pose two, arms crossed"></div>
      <div class="front__pose front__pose--three" role="img" aria-label="Model pose three, waving"></div>
    </div>
    <div class="ribbon front__ribbon"></div>
    <div class="band front__band"></div>
    <div class="bow front__bow" role="img" aria-label="Satin pink ribbon bow"></div>
    <div class="front__wordmark">Breezy Plum</div>
  </section>

  <section class="card card--back">
    <div class="ribbon back__ribbon"></div>
    <div class="band back__band"></div>
    <div class="bow back__bow" role="img" aria-label="Satin pink ribbon bow tied on the band"></div>
    <div class="back__wordmark">Breezy Plum</div>
    <div class="back__name">Maddie Lorne</div>
    <ul class="back__contact">
      <li>(07) 35517204</li>
      <li>admin@breezyplum.com.au</li>
      <li>www.breezyplum.com.au</li>
    </ul>
  </section>
</body>
</html>
```